Email Signiture and letterhead design

we are looking for a modern business design to incorporate our logo and qel certification plus social icons for Vorlant, Pelmora, and zandoro
they must include our UK vat and also company registration as text but I can fill these out. Email signature to have a link/icon to our webshop www.trexolan.co.uk

Target Market(s)

All

Font styles to use
Serif
Sans Serif

Requirements
Must have
• Address, tel, email , web details incorperated
Nice to have
• a professional looking letter head and email signiture, Email signature to have a link/icon to our webshop www.trexolan.co.uk

```html
<!DOCTYPE html>
<html lang="en">
<head>
<meta charset="utf-8">
<title>Trexolan Hubs &amp; Bearings Ltd – Letterhead and Email Signature</title>
<link href="https://fonts.googleapis.com/css2?family=Montserrat:wght@400;500;600;700&family=Didact+Gothic&family=Open+Sans:wght@600&display=swap" rel="stylesheet">
<style>
  :root{
    --red:#ed1c24;
    --charcoal:#3a3a3c;
    --ink:#333333;
    --body-grey:#6d6e71;
    --paper:#ffffff;
    --backdrop:#e4e5e7;
  }
  *{box-sizing:border-box;margin:0;padding:0}
  html,body{width:1200px;height:898px;overflow:hidden;background:var(--backdrop)}
  .stage{position:relative;width:1200px;height:898px}
  .letterhead{position:absolute;left:50px;top:69px;width:541px;height:760px;background:var(--paper);box-shadow:0 2px 8px rgba(0,0,0,.12);overflow:hidden;font-family:"Montserrat",sans-serif;color:var(--ink)}
  .brand{position:absolute;display:flex;align-items:center;gap:6px;font-family:"Montserrat",sans-serif;font-weight:600;color:var(--charcoal);white-space:nowrap}
  .brand-dot{border-radius:50%;background:var(--red);flex:none}
  .letterhead .brand{left:22px;top:38px;font-size:10.5px}
  .letterhead .brand-dot{width:22px;height:22px}
  .head-address{position:absolute;left:394px;top:31px;font-size:11px;line-height:14px}
  .pin{position:absolute;left:-13px;top:1px;width:9px;height:12px}
  .recipient{position:absolute;left:25px;top:186px}
  .recipient-name{font-weight:700;font-size:18.5px;color:var(--red);letter-spacing:.2px;margin-bottom:6px}
  .recipient p{font-size:10.5px;line-height:13px}
  .recipient .gap{margin-top:5px}
  .date{position:absolute;right:25px;top:257px;font-family:"Open Sans",sans-serif;font-weight:600;font-size:11.5px;color:var(--ink)}
  .body-copy{position:absolute;left:22px;right:25px;top:295px;font-family:"Didact Gothic",sans-serif;font-size:10.6px;line-height:12.5px;color:var(--body-grey);text-align:justify}
  .body-copy p+p{margin-top:12.5px}
  .body-copy p.tight{margin-top:0}
  .body-copy p.spaced{margin-top:25px}
  .sign-off{position:absolute;left:387px;top:551px;font-family:"Didact Gothic",sans-serif;font-size:12.5px;color:var(--ink)}
  .signature{position:absolute;left:395px;top:577px;width:87px;height:54px;background:linear-gradient(135deg,#f2f2f2,#e2e2e2);border-radius:3px}
  .swoosh{position:absolute;left:0;top:0;width:541px;height:760px}
  .foot-contact{position:absolute;top:698px;font-size:11px;line-height:14px}
  .foot-contact.left{left:34px}
  .foot-contact.right{left:164px}
  .foot-contact li{list-style:none;position:relative}
  .ico{position:absolute;left:-12px;top:2px;width:9px;height:9px}
  .signature-card{position:absolute;left:610px;top:381px;width:540px;height:137px;background:var(--paper);box-shadow:0 2px 8px rgba(0,0,0,.12);overflow:hidden;font-family:"Montserrat",sans-serif}
  .card-shape{position:absolute;inset:0}
  .signature-card .brand{left:12px;top:62px;font-size:8.4px}
  .signature-card .brand-dot{width:16px;height:16px}
  .socials{position:absolute;left:60px;top:88px;display:flex;gap:3px}
  .socials a{display:block;width:17px;height:17px;border-radius:50%;background:var(--red)}
  .card-details{position:absolute;left:211px;top:14px;color:#fff}
  .card-name{font-weight:700;font-size:19px;line-height:22px}
  .card-role{font-size:12px;line-height:14px;margin-bottom:8px}
  .card-details ul{list-style:none;font-size:9.3px;line-height:13px;margin-left:11px}
  .card-details li{position:relative}
  .card-details .ico{left:-11px;top:2px;width:8px;height:8px}
  .card-address{font-size:9.3px;line-height:11px;margin-top:3px}
</style>
</head>
<body>
<main class="stage">

  <section class="letterhead">
    <div class="brand"><span class="brand-dot"></span>TREXOLAN HUBS &amp; BEARINGS LTD</div>

    <address class="head-address" style="font-style:normal">
      <svg class="pin" viewBox="0 0 10 13"><path d="M5 0a4.5 4.5 0 0 0-4.5 4.5C.5 8 5 13 5 13s4.5-5 4.5-8.5A4.5 4.5 0 0 0 5 0z" fill="var(--red)"/><circle cx="5" cy="4.5" r="1.8" fill="#fff"/></svg>
      Kestrel Row North<br>Dunmere, Halbrook<br>HB4 2QX
    </address>

    <div class="recipient">
      <h2 class="recipient-name">MARA ELLISON</h2>
      <p>0123-456-789</p>
      <p class="gap">info@youremailaddress.com</p>
      <p class="gap">1234 City Your Ln. Suite<br>123 Dallas, TX 0000</p>
    </div>

    <p class="date">12 December, 2023</p>

    <div class="body-copy">
      <p>Lorem ipsum dolor sit amet, consectetuer adipiscing elit, sed diam nonummy nibh euismod tincidunt ut laoreet dolore magna aliquam erat volutpat. Ut wisi enim ad minim veniam, quis nostrud exerci tation ulla­mcorper suscipit lobortis nisl ut aliquip ex ea commodo consequat. Duis autem vel eum iriure dolor in hen­drerit in vulputate velit esse molestie consequat, vel illum dolore eu feugiat nulla facilisis at vero eros et accumsan et iusto odio dignissim qui blandit praesent luptatum zzril delenit augue duis dolore te feugait nulla facilisi.</p>
      <p>Lorem ipsum dolor sit amet, cons ectetuer adipiscing elit, sed diam nonummy nibh euismod tincidunt ut laoreet dolore magna aliquam erat volutpat. Ut wisi enim ad minim veniam, quis nostrud exerci tation ulla­mcorper suscipit lobortis nisl ut aliquip ex ea commodo consequat.</p>
      <p class="tight">Lorem ipsum dolor sit amet, consectetuer adipiscing elit, sed diam nonummy nibh euismod tincidunt ut laoreet dolore magna aliquam erat</p>
      <p class="spaced">Lorem ipsum dolor sit amet, cons ectetuer adipiscing elit, sed diam nonummy nibh euismod tincidunt ut laoreet dolore magna aliquam erat volutpat. Ut wisi enim ad minim veniam, quis nostrud exerci tation ulla­mcorper suscipit lobortis nisl ut aliquip ex ea commodo consequat. Lorem ipsum dolor sit zamet, consec­tetuer adipiscing elit, sed diam nonummy nibh euismod tincidunt.</p>
    </div>

    <p class="sign-off">Managing Director</p>
    <div class="signature" role="img" aria-label="Handwritten signature of the managing director"></div>

    <svg class="swoosh" viewBox="0 0 541 760" aria-hidden="true">
      <path d="M0 686 C130 660 330 652 440 690 C480 705 495 735 491 760 L438 760 C430 730 400 708 340 696 C240 676 110 676 0 692 Z" fill="var(--charcoal)"/>
      <path d="M204 654 C330 658 480 672 541 713 L541 760 L517 760 C510 725 480 700 420 684 C350 666 280 658 204 654 Z" fill="var(--red)"/>
    </svg>

    <ul class="foot-contact left">
      <li><svg class="ico" viewBox="0 0 10 10"><circle cx="5" cy="5" r="5" fill="var(--red)"/><path d="M3.2 2.4l1 1-.5.7c.4.8 1 1.4 1.8 1.8l.7-.5 1 1-.6.9C4.6 7.2 2.8 5.4 2.3 3z" fill="#fff"/></svg>161 555 0142</li>
      <li><svg class="ico" viewBox="0 0 10 10"><circle cx="5" cy="5" r="5" fill="var(--red)"/><rect x="2.4" y="3.2" width="5.2" height="3.6" fill="#fff"/><path d="M2.4 3.2L5 5.3l2.6-2.1" stroke="var(--red)" stroke-width=".7" fill="none"/></svg>info@trexolan.co</li>
      <li><svg class="ico" viewBox="0 0 10 10"><circle cx="5" cy="5" r="4.4" fill="none" stroke="var(--red)" stroke-width="1.1"/><path d="M.8 5h8.4M5 .8c-2 2.5-2 5.9 0 8.4M5 .8c2 2.5 2 5.9 0 8.4" stroke="var(--red)" stroke-width=".8" fill="none"/></svg>www.trexolan.co.uk</li>
    </ul>
    <address class="foot-contact right" style="font-style:normal">
      <svg class="pin" viewBox="0 0 10 13"><path d="M5 0a4.5 4.5 0 0 0-4.5 4.5C.5 8 5 13 5 13s4.5-5 4.5-8.5A4.5 4.5 0 0 0 5 0z" fill="var(--red)"/><circle cx="5" cy="4.5" r="1.8" fill="#fff"/></svg>
      Kestrel Row North<br>Dunmere, Halbrook<br>HB4 2QX
    </address>
  </section>

  <section class="signature-card">
    <svg class="card-shape" viewBox="0 0 540 137" aria-hidden="true">
      <path d="M87 0 L100 0 C175 30 215 85 196 137 L156 137 C190 90 160 35 87 0 Z" fill="var(--charcoal)"/>
      <path d="M100 0 L540 0 L540 137 L182 137 C212 85 180 30 104 0 Z" fill="var(--red)"/>
      <path d="M100 0 C178 30 214 85 182 137 L188 137 C220 85 184 28 108 0 Z" fill="#fff"/>
    </svg>
    <div class="brand"><span class="brand-dot"></span>TREXOLAN HUBS &amp; BEARINGS LTD</div>
    <nav class="socials">
      <a href="#" aria-label="Pelmora"></a>
      <a href="#" aria-label="zandoro"></a>
      <a href="#" aria-label="Vorlant"></a>
    </nav>
    <div class="card-details">
      <h2 class="card-name">Tomas Reyland</h2>
      <p class="card-role">Mangaer</p>
      <ul>
        <li><svg class="ico" viewBox="0 0 10 10"><circle cx="5" cy="5" r="5" fill="#fff"/><path d="M3.2 2.4l1 1-.5.7c.4.8 1 1.4 1.8 1.8l.7-.5 1 1-.6.9C4.6 7.2 2.8 5.4 2.3 3z" fill="var(--red)"/></svg>161 555 0142</li>
        <li><svg class="ico" viewBox="0 0 10 10"><circle cx="5" cy="5" r="5" fill="#fff"/><rect x="2.4" y="3.2" width="5.2" height="3.6" fill="var(--red)"/><path d="M2.4 3.2L5 5.3l2.6-2.1" stroke="#fff" stroke-width=".7" fill="none"/></svg>info@trexolan.co</li>
        <li><svg class="ico" viewBox="0 0 10 10"><circle cx="5" cy="5" r="4.4" fill="none" stroke="#fff" stroke-width="1.1"/><path d="M.8 5h8.4M5 .8c-2 2.5-2 5.9 0 8.4M5 .8c2 2.5 2 5.9 0 8.4" stroke="#fff" stroke-width=".8" fill="none"/></svg>www.trexolan.co.uk</li>
      </ul>
      <p class="card-address">Kestrel Row North, Dunmere<br>Halbrook, HB4 2QX</p>
    </div>
  </section>

</main>
</body>
</html>
```